Vorrel Sports Nutrition Brand needs a Packaging label

Hi all, please see the considerations for our vision.
We need a Golden Ratio packaging label design for new Sports nutrition/supplement brand. I would like to give you a little bit of background about myself and hopefully that will help you in creating the design.
I am myself into fitness. I am 33 years old at the moment and been hitting gyms consistently from 14 years old. I do use supplements of all types that helps with performance and body compositions.
Ideally I would like the brand to be able to resonate with male and female audience. The brand needs to give premium look and feel. Those people who will be associating themselves with the brand should be proud of themselves being a part of the team. That's our ideal customer persona.
In terms of colours we are open to your suggestions but do think that red should be included as a detail colour.
P.S Please check out my Instagram to learn more about ideal customer for the brand. @pamodeyxx
When creating the name ''vorrel'' we wanted the name to capture two things. First a feeling that we get when we go to gyms and the feeling is excited. And secondly the name for the product or the industry and that's nutrition. We then shortened the feeling excited to Vorrel for a more catchy name.

The Nutrition information will be sent to add once we pick the design.
The pictures of brands that we admire them are attached.

Please design One label design and just resize for these products. For dimensions please refer to the Print guide attached.
Bulk Core Builder 2.25KG
Tasty Creatine 250G
Vigor Lift Prime 120 Tabs
Surge Flow Pre Workout 250G
Branded Shakers

Target Market(s)

Fitness / bodybuilding audience male & female mass market

Industry/Entity Type

Nutrition

Colors

Designer to choose colors to be used in the design.

Requirements
Must have
• Our logo.
• Please find it attached
Nice to have
• The transparent Logo X some where in the background almost like a watermark. In other words like a subconscious clue.
Should not have
• Organic look.

```html
<!DOCTYPE html>
<html lang="en">
<head>
<meta charset="utf-8">
<title>Vorrel Nutrition – Vigor Lift Prime Label</title>
<link href="https://fonts.googleapis.com/css2?family=Titan+One&family=Archivo+Black&display=swap" rel="stylesheet">
<style>
  :root {
    --page: #ffffff;
    --blue-deep: #12408f;
    --blue-mid: #1f7fcf;
    --blue-light: #2fc2ec;
    --red-deep: #7d0f16;
    --red: #c8202a;
    --black: #141416;
    --yellow: #fff200;
    --gold: #f7c41a;
    --steel-dark: #3c3c40;
    --steel-light: #f0f0f2;
    --white: #ffffff;
  }
  html, body {
    margin: 0;
    padding: 0;
    width: 1200px;
    height: 1200px;
    overflow: hidden;
    background: var(--page);
  }
  .canvas {
    position: relative;
    width: 1200px;
    height: 1200px;
  }
  .label {
    position: absolute;
    left: 110px;
    width: 981px;
    height: 427px;
    overflow: hidden;
  }
  .label--wave { top: 128px; }
  .label--band { top: 632px; }
  .label svg { display: block; width: 100%; height: 100%; }
  .brand-name {
    font-family: "Archivo Black", sans-serif;
    fill: var(--white);
  }
  .title-block {
    font-family: "Titan One", sans-serif;
  }
</style>
</head>
<body>
<main class="canvas">

  <!-- Label variant one: wave base -->
  <section class="label label--wave">
    <svg viewBox="0 0 981 427" xmlns="http://www.w3.org/2000/svg">
      <defs>
        <linearGradient id="waveSky" x1="0" y1="0" x2="1" y2="1">
          <stop offset="0" stop-color="var(--blue-deep)"/>
          <stop offset="0.3" stop-color="var(--blue-light)"/>
          <stop offset="0.7" stop-color="var(--blue-mid)"/>
          <stop offset="1" stop-color="var(--blue-deep)"/>
        </linearGradient>
        <linearGradient id="steel" x1="0" y1="0" x2="1" y2="0">
          <stop offset="0" stop-color="var(--steel-dark)"/>
          <stop offset="0.45" stop-color="var(--steel-light)"/>
          <stop offset="1" stop-color="#6a6a70"/>
        </linearGradient>
        <linearGradient id="redBand" x1="0" y1="0" x2="1" y2="0">
          <stop offset="0" stop-color="var(--red-deep)"/>
          <stop offset="0.5" stop-color="var(--red)"/>
          <stop offset="1" stop-color="var(--red-deep)"/>
        </linearGradient>
        <linearGradient id="blueBox" x1="0" y1="0" x2="0" y2="1">
          <stop offset="0" stop-color="var(--blue-mid)"/>
          <stop offset="0.6" stop-color="var(--blue-light)"/>
          <stop offset="1" stop-color="var(--blue-deep)"/>
        </linearGradient>
        <linearGradient id="chromeBlue" x1="0" y1="0" x2="0" y2="1">
          <stop offset="0" stop-color="#1560c8"/>
          <stop offset="0.5" stop-color="var(--blue-light)"/>
          <stop offset="0.52" stop-color="#0d3a8a"/>
          <stop offset="1" stop-color="var(--blue-mid)"/>
        </linearGradient>
        <linearGradient id="goldNum" x1="0" y1="0" x2="0" y2="1">
          <stop offset="0" stop-color="var(--yellow)"/>
          <stop offset="0.5" stop-color="#fff8b0"/>
          <stop offset="1" stop-color="var(--gold)"/>
        </linearGradient>
      </defs>

      <rect class="label-ground" width="981" height="427" fill="url(#waveSky)"/>

      <!-- steel wave base -->
      <path class="wave-base" d="M0 372 C120 320 250 330 380 375 C470 405 540 390 600 370 L600 427 L0 427 Z" fill="url(#steel)"/>
      <path d="M0 372 C120 320 250 330 380 375 C470 405 540 390 600 370" fill="none" stroke="var(--red)" stroke-width="4"/>
      <path class="wave-base" d="M790 360 C840 345 900 350 981 370 L981 427 L790 427 Z" fill="url(#steel)"/>
      <path d="M790 360 C840 345 900 350 981 370" fill="none" stroke="var(--red)" stroke-width="4"/>

      <!-- athlete figure area -->
      <rect x="266" y="52" width="120" height="304" rx="40" fill="var(--red)" opacity="0.85" role="img" aria-label="Red silhouette of a female athlete running"/>

      <!-- brand name -->
      <g class="brand" transform="translate(486 376) rotate(-90)">
        <text class="brand-name" x="0" y="0" font-size="80" textLength="340" lengthAdjust="spacingAndGlyphs">VORREL</text>
        <text class="brand-name" x="112" y="26" font-size="17" textLength="188" lengthAdjust="spacing">NUTRITION</text>
      </g>

      <!-- product band -->
      <rect x="554" y="0" width="236" height="427" fill="url(#redBand)"/>
      <rect x="554" y="0" width="3" height="427" fill="var(--blue-light)"/>
      <rect x="561" y="0" width="2" height="427" fill="var(--blue-deep)"/>
      <rect x="787" y="0" width="3" height="427" fill="var(--blue-light)"/>
      <rect x="781" y="0" width="2" height="427" fill="var(--blue-deep)"/>

      <g class="title-block" text-anchor="middle" fill="url(#chromeBlue)" stroke="#9fd9ff" stroke-width="1.2">
        <text x="672" y="88" font-size="64" transform="skewX(-12) translate(18 0)">VIGOR</text>
        <text x="672" y="140" font-size="42" transform="skewX(-12) translate(28 0)">LIFT</text>
        <text x="672" y="204" font-size="62" transform="skewX(-12) translate(42 0)">PRIME</text>
      </g>

      <rect x="642" y="254" width="135" height="190" rx="14" fill="url(#blueBox)"/>
      <g class="title-block" text-anchor="middle">
        <text x="710" y="340" font-size="72" fill="url(#goldNum)" stroke="var(--red-deep)" stroke-width="1.5">30</text>
        <text x="710" y="371" font-size="18" fill="url(#goldNum)" stroke="var(--red-deep)" stroke-width="0.8">CAPSULES</text>
      </g>
    </svg>
  </section>

  <!-- Label variant two: chrome rails -->
  <section class="label label--band">
    <svg viewBox="0 0 981 427" xmlns="http://www.w3.org/2000/svg">
      <defs>
        <linearGradient id="railSteel" x1="0" y1="0" x2="1" y2="0">
          <stop offset="0" stop-color="var(--steel-dark)"/>
          <stop offset="0.5" stop-color="var(--steel-light)"/>
          <stop offset="1" stop-color="var(--steel-dark)"/>
        </linearGradient>
        <linearGradient id="bandSky" x1="0" y1="0" x2="0" y2="1">
          <stop offset="0" stop-color="var(--blue-deep)"/>
          <stop offset="0.35" stop-color="var(--blue-mid)"/>
          <stop offset="0.55" stop-color="var(--blue-light)"/>
          <stop offset="1" stop-color="var(--blue-deep)"/>
        </linearGradient>
        <linearGradient id="redPanel" x1="0" y1="0" x2="1" y2="0">
          <stop offset="0" stop-color="var(--red-deep)"/>
          <stop offset="0.5" stop-color="var(--red)"/>
          <stop offset="1" stop-color="var(--red-deep)"/>
        </linearGradient>
        <linearGradient id="goldText" x1="0" y1="0" x2="0" y2="1">
          <stop offset="0" stop-color="var(--yellow)"/>
          <stop offset="0.5" stop-color="#fff8b0"/>
          <stop offset="1" stop-color="var(--gold)"/>
        </linearGradient>
      </defs>

      <rect width="981" height="427" fill="url(#bandSky)"/>

      <!-- product panel -->
      <rect x="570" y="28" width="411" height="374" fill="url(#redPanel)"/>
      <polygon points="562,80 770,28 981,28 981,142 562,280" fill="var(--black)"/>
      <line x1="562" y1="80" x2="770" y2="28" stroke="var(--yellow)" stroke-width="2"/>
      <line x1="562" y1="280" x2="981" y2="142" stroke="var(--yellow)" stroke-width="2"/>
      <rect x="570" y="28" width="3" height="374" fill="var(--blue-light)"/>
      <rect x="576" y="28" width="2" height="374" fill="var(--blue-deep)"/>
      <rect x="816" y="28" width="2" height="374" fill="var(--blue-light)"/>
      <rect x="821" y="28" width="2" height="374" fill="var(--blue-deep)"/>

      <!-- chrome rails -->
      <rect x="0" y="0" width="981" height="30" fill="url(#railSteel)"/>
      <rect x="0" y="12" width="981" height="3" fill="#ffffff" opacity="0.6"/>
      <rect x="0" y="400" width="981" height="27" fill="url(#railSteel)"/>
      <rect x="0" y="410" width="981" height="3" fill="#ffffff" opacity="0.6"/>

      <!-- athlete figure area -->
      <rect x="256" y="56" width="120" height="308" rx="40" fill="var(--red)" stroke="var(--yellow)" stroke-width="3" role="img" aria-label="Red silhouette of a female athlete running with yellow rim light"/>

      <!-- brand name -->
      <g class="brand" transform="translate(486 384) rotate(-90)">
        <text class="brand-name" x="0" y="0" font-size="80" textLength="336" lengthAdjust="spacingAndGlyphs">VORREL</text>
        <text class="brand-name" x="116" y="26" font-size="17" textLength="184" lengthAdjust="spacing">NUTRITION</text>
      </g>

      <g class="title-block" text-anchor="middle" fill="url(#goldText)" stroke="var(--red-deep)" stroke-width="1.2">
        <text x="665" y="108" font-size="46" transform="rotate(-15 665 96)">Vigor</text>
        <text x="690" y="160" font-size="46" transform="rotate(-15 690 144)">Lift</text>
        <text x="705" y="212" font-size="46" transform="rotate(-15 705 196)">Prime</text>
      </g>

      <g class="title-block" text-anchor="middle" fill="url(#goldText)" stroke="var(--blue-mid)" stroke-width="1.5">
        <text x="722" y="340" font-size="88">30</text>
        <text x="726" y="380" font-size="22" stroke-width="0.8">CAPSULES</text>
      </g>
    </svg>
  </section>

</main>
</body>
</html>
```